Prominent Law Firm Needs a New Stationary Design

We need new stationary design to go with our new logo and rustic offices.
Things we need on the letterhead:
logo (see attached file), would also like the Seven-Figure Verdict Logo (attached) somewhere on the stationary,
5182 North Pelham Avenue
Tulsa, Oklahoma 74219
(918) 555-0143 Tel ★ (918) 555-0187 Fax
www.TWVQX.example

We also need the names of the 4 partners:
Dale K. Hollingsworth
Vernon P. Hollingsworth
Mark E. Fenwicke
Tyler D. Ashcombe

And the other staff:
Brenda K. Lyle
Tendaji K. Oyelowanta
Gordon Pettijo

Hilda V. Pruitt, RN

Of Counsel:
Wendell S. Hollingsworth

Industry/Entity Type

Law Firm

```html
<!DOCTYPE html>
<html lang="en">
<head>
<meta charset="utf-8">
<title>Hollingsworth Hollingsworth Fenwicke — Stationery</title>
<link href="https://fonts.googleapis.com/css2?family=Open+Sans:wght@400;700&family=PT+Serif:wght@400;700&display=swap" rel="stylesheet">
<style>
  :root {
    --bg: #ececec;
    --paper: #ffffff;
    --ink: #2a2a2a;
    --body-ink: #555555;
    --muted: #777777;
    --card: #2b2b2b;
    --card-ink: #f2f2f2;
    --card-soft: #cfcfcf;
  }
  * { box-sizing: border-box; margin: 0; padding: 0; }
  html, body { width: 1200px; height: 900px; overflow: hidden; }
  body { background: var(--bg); font-family: "Open Sans", sans-serif; position: relative; }

  .letterhead {
    position: absolute; left: 60px; top: 20px; width: 664px; height: 860px;
    background: var(--paper); box-shadow: 0 2px 10px rgba(0,0,0,.12);
    padding: 40px 56px 0; color: var(--body-ink);
  }
  .firm-mark { text-align: center; margin-bottom: 30px; }
  .firm-mark__name {
    font-family: "PT Serif", serif; font-weight: 700; font-size: 15px;
    letter-spacing: 1.5px; text-transform: uppercase; color: var(--ink);
  }
  .firm-mark__initials {
    display: inline-flex; align-items: center; gap: 10px; margin-top: 4px;
    font-family: "PT Serif", serif; font-weight: 700; font-size: 34px; color: var(--ink);
  }
  .firm-mark__dot { width: 10px; height: 10px; border-radius: 50%; background: var(--ink); }

  .letterhead__body { display: flex; gap: 24px; }

  .roster { width: 148px; flex: none; font-family: "PT Serif", serif; font-size: 10.5px;
    line-height: 1.5; color: var(--ink); border-right: 1px solid #d6d6d6; padding-right: 12px; }
  .roster__group { margin-bottom: 14px; }
  .roster__label { font-size: 9px; letter-spacing: 1px; text-transform: uppercase;
    color: var(--muted); margin-bottom: 3px; }

  .letter { flex: 1; }
  .letter__salutation { font-weight: 700; font-size: 12px; color: var(--ink); margin-bottom: 10px; }
  .letter__para { font-size: 11px; line-height: 1.55; margin-bottom: 12px; }
  .letter__closing { margin-top: 16px; font-size: 11.5px; }
  .signature { width: 170px; height: 34px; margin-bottom: 6px; border-radius: 17px;
    background: linear-gradient(90deg, rgba(47,95,143,.25), rgba(47,95,143,.08)); }
  .letter__signer { color: var(--ink); font-weight: 700; }

  .verdict-mark { position: absolute; left: 56px; bottom: 48px; display: flex; align-items: center;
    gap: 8px; font-family: "PT Serif", serif; font-weight: 700; font-size: 11px; color: var(--ink); width: 150px; }
  .verdict-mark__dot { width: 22px; height: 22px; flex: none; border-radius: 50%; background: var(--ink); }

  .letter-footer {
    position: absolute; right: 56px; bottom: 40px; width: 340px;
    font-family: "PT Serif", serif; font-size: 11.5px; line-height: 1.55; color: var(--ink); text-align: center;
  }
  .divider { position: relative; height: 1px; background: var(--ink); margin-bottom: 8px; }
  .divider::after { content: ""; position: absolute; left: 50%; top: -3px; width: 7px; height: 7px;
    margin-left: -3.5px; border-radius: 50%; background: currentColor; }

  .card {
    position: absolute; left: 770px; width: 390px; height: 222px;
    background: var(--card); color: var(--card-ink); padding: 9px;
    box-shadow: 0 3px 10px rgba(0,0,0,.25);
  }
  .card__frame { width: 100%; height: 100%; border: 1px solid var(--card-soft);
    display: flex; flex-direction: column; align-items: center; justify-content: center; text-align: center; padding: 0 10px; }
  .card--back { top: 170px; }
  .card--front { top: 450px; }
  .card .firm-mark__name { color: var(--card-ink); font-size: 13px; }
  .card .firm-mark__initials { color: var(--card-ink); font-size: 40px; }
  .card .firm-mark__dot { background: var(--card-ink); }
  .card__person { font-family: "PT Serif", serif; font-weight: 700; font-size: 18px; margin-top: 10px; }
  .card__title { font-family: "PT Serif", serif; font-size: 13px; color: var(--card-soft); margin-top: 2px; }
  .card .divider { width: 250px; background: var(--card-soft); color: var(--card-ink); margin: 12px 0 9px; }
  .card__contacts { font-family: "PT Serif", serif; font-size: 10.5px; color: var(--card-soft);
    display: flex; gap: 14px; white-space: nowrap; }
  .card__address { font-family: "PT Serif", serif; font-size: 10.5px; color: var(--card-soft); margin-top: 6px; }
</style>
</head>
<body>
  <section class="letterhead">
    <header class="firm-mark">
      <div class="firm-mark__name">Hollingsworth Hollingsworth Fenwicke</div>
      <div class="firm-mark__initials"><span class="firm-mark__dot"></span>HHF</div>
    </header>

    <div class="letterhead__body">
      <aside class="roster">
        <div class="roster__group">
          <div class="roster__label">Partners</div>
          <div>Dale K. Hollingsworth</div>
          <div>Vernon P. Hollingsworth</div>
          <div>Mark E. Fenwicke</div>
          <div>Tyler D. Ashcombe</div>
        </div>
        <div class="roster__group">
          <div class="roster__label">Associates</div>
          <div>Brenda K. Lyle</div>
          <div>Tendaji K. Oyelowanta</div>
          <div>Gordon Pettijo</div>
        </div>
        <div class="roster__group">
          <div>Hilda V. Pruitt, RN</div>
        </div>
        <div class="roster__group">
          <div class="roster__label">Of Counsel</div>
          <div>Wendell S. Hollingsworth</div>
        </div>
      </aside>

      <article class="letter">
        <p class="letter__salutation">Lorem Ipsum,</p>
        <p class="letter__para">Cras mattis consectetur purus sit amet fermentum. Etiam porta sem malesuada magna mollis euismod. Integer posuere erat a ante venenatis dapibus posuere velit aliquet. Cras justo odio, dapibus ac facilisis in, egestas eget quam.</p>
        <p class="letter__para">Vivamus sagittis lacus vel augue laoreet rutrum faucibus dolor auctor. Donec sed odio dui. Etiam porta sem malesuada magna mollis euismod. Morbi leo risus, porta ac consectetur ac, vestibulum at eros.</p>
        <p class="letter__para">Donec id elit non mi porta gravida at eget metus. Fusce dapibus, tellus ac cursus commodo, tortor mauris condimentum nibh, ut fermentum massa justo sit amet risus. Cum sociis natoque penatibus et magnis dis parturient montes.</p>
        <p class="letter__para">Curabitur blandit tempus porttitor. Aenean lacinia bibendum nulla sed consectetur. Morbi leo risus, porta ac consectetur ac, vestibulum at eros. Nullam quis risus eget urna mollis ornare vel eu leo.</p>
        <div class="letter__closing">
          <div class="signature" role="img" aria-label="Handwritten signature of Dale K. Hollingsworth"></div>
          <div class="letter__signer">Dale K. Hollingsworth</div>
          <div>Chairman &amp; CEO</div>
        </div>
      </article>
    </div>

    <div class="verdict-mark"><span class="verdict-mark__dot"></span><span>Seven-Figure Verdict Logo</span></div>

    <footer class="letter-footer">
      <div class="divider"></div>
      <div>5182 North Pelham Avenue, Tulsa, Oklahoma 74219</div>
      <div>(918) 555-0143 Tel ★ (918) 555-0187 Fax</div>
      <div>www.TWVQX.example</div>
    </footer>
  </section>

  <section class="card card--back">
    <div class="card__frame">
      <div class="firm-mark__name">Hollingsworth Hollingsworth Fenwicke</div>
      <div class="firm-mark__initials"><span class="firm-mark__dot"></span>HHF</div>
    </div>
  </section>

  <section class="card card--front">
    <div class="card__frame">
      <div class="firm-mark__name">Hollingsworth Hollingsworth Fenwicke</div>
      <div class="card__person">Dale K. Hollingsworth</div>
      <div class="card__title">Chairman &amp; CEO</div>
      <div class="divider"></div>
      <div class="card__contacts"><span>dale@twvqx.example</span><span>(918) 555-0143</span><span>www.TWVQX.example</span></div>
      <div class="card__address">5182 North Pelham Avenue, Tulsa, Oklahoma 74219</div>
    </div>
  </section>
</body>
</html>
```